Need a Middle Eastern/Cooking/Nutrition Design please :)

Hi I am looking to revamp my Middle Eastern/Cooking/Nutrition Blog for something that is clean, sophisticated yet sultry. My site now www.plumhavenkitchen.com is messy and needs more color help with background. Please send anything you think is suitable for the concept.
Target Market(s)
high end
Industry/Entity Type
Nutrition
Requirements
Must have
- Your work looks wonderful!
I am looking forward to your designs! I am really trying to revamp my current site www.plumhavenkitchen.com to be more clean and sophisticated.
I like this color palette or maybe royal purple and gold. http://www.hueweavers.net/palette/418205/Amber_Dunes
I had my website evaluated by a brand specialist and this what she said I should be doing :) Let me know what you think- really appreciate it!
Comments Below:
Given your brand identity, I think you want to go for something clean and simple but with touches of bold color and iconography. You want the site to come off as approachable, but to also have an exotic and slightly mysterious edge. Perhaps choose a solid background color and use stylish icons, flourishes and images to bring the Middle Eastern/Mediterranean flavor.
I also recommend that you use a neutral color or a whitewashed design as your background. It is easier on the eyes to read a lot of text when it’s a neutral (light or white) background color with a darker font.
Here is a color palette that I like for you: http://www.hueweavers.net/palette/418205/Amber_Dunes
In terms of organization, I think it would be great to have your home page be a jump page. So, rather than having a list of your recent posts, perhaps you can welcome guests with a picture of yourself/your food/your brand.
Then, you could have a menu of options for people to explore your site (kind of like the bar you have at the top of your page now). But instead of just having the text, you could use images as the links to the different pages. This would include a link to classes, recipes, nutritional information, products, TV shows/videos, bio, etc. And you could organize it in a creative way on the page.
There are so many ways that you can organize your site, and it’s completely up to you! But here are some examples that I think you could look to for inspiration:
http://marisolvantrecca.com/
http://www.willowbrookhostess.com/
http://www.dunavelm.com/
http://www.trylentilo.com/trylentilo.com/Lentilo.html
http://www.korvidash.com/
http://www.bresklunch.com/
For your brand name, ultimately, you want something that reflects the down to earth yet somewhat exotic nature of your brand. The actual brand name is up to you…but I do like where you’re going with the ingredients.
I want simple and sophisticated yet also portrays the mysterious and exotic Middle East. The site colors and pictures should transport people but also want it clean. I think my site is too busy now.
The content and layout could be the same but the logo, domain name possible and website name, background and color scheme all have to change although I do like dark purple and gold as possibilities along with the color pattern I sent already,
Im not sure if its a single page or full project but I do want a total revamp of the scheme- do you need to redo the website or just remake the existing because I can provide the website info if thats the case . I can pay the up front cost now. I believe the quote is 300.
Also im not sure if I should stick with the Sprig up name or here are other name options if you think they meet the sophisticated brand of the Middle East more.
tahini & honey
fig & chickpea
saffron & rosewater- very exotic
harissa & honey
pomegranates & pistachios
saffron & pomegranates
figs & saffron
The name should be playful and fun for the site. I like the idea of ingredients because it brings both the Mediterranean and Middle East imagery and allows for broad appeal.
Thank you soooooooooo much- I know it’s a lot to think about and I greatly appreciate your insight and talents in this!!
Nice to have
- Clean, sophisticated, sultry, exotic and professional
Should not have
- too busy

```html
<!DOCTYPE html>
<html lang="en">
<head>
<meta charset="utf-8">
<title>Sprig up – Taste of the Mediterranean &amp; Middle East</title>
<link href="https://fonts.googleapis.com/css2?family=PT+Sans:wght@400;700&family=Ubuntu:wght@400;500&display=swap" rel="stylesheet">
<style>
:root{
  --header-top:#8f5a58;
  --header-bottom:#9b6361;
  --nav-band:#7b4b49;
  --nav-text:#ffffff;
  --page-dark:#2e2725;
  --footer:#242120;
  --footer-base:#332a28;
  --panel:#ffffff;
  --ink:#2b2b2b;
  --muted:#4a4a4a;
  --rule:#c9c9c9;
  --paper:#efe3b6;
  --sun-top:#f7da3a;
  --sun-bottom:#f3a72a;
  --leaf-top:#9fcf4a;
  --leaf-bottom:#6aa82c;
  --field:#b07f7c;
}
*{box-sizing:border-box;margin:0;padding:0}
html,body{width:959px;height:1200px;overflow:hidden}
body{position:relative;background:var(--page-dark);font-family:"PT Sans",sans-serif;color:var(--ink)}
.site-header{position:absolute;left:0;top:0;width:959px;height:385px;background:linear-gradient(var(--header-top),var(--header-bottom))}
.brand{position:absolute;left:30px;top:60px;width:340px;text-align:center}
.brand-name{font-family:"Ubuntu",sans-serif;font-weight:400;font-size:62px;color:#fff;letter-spacing:2px;line-height:1}
.brand-band{margin:40px auto 0;width:276px;height:42px;background:#f4f4f4;display:flex;align-items:center;justify-content:center;font-size:8px;letter-spacing:.3px;color:#555}
.subscribe{position:absolute;left:91px;top:297px;width:200px;text-align:center}
.subscribe-title{font-family:"Ubuntu",sans-serif;font-size:14px;color:#fff;margin-bottom:9px}
.subscribe-field{width:200px;height:33px;background:var(--field);border:1px solid #c9a3a0;color:#f4e8e7;font-size:11px;text-align:left;padding:9px 11px}
.hero-frame{position:absolute;left:405px;top:20px;width:530px;height:335px;background:#fff;padding:15px;box-shadow:4px 8px 10px rgba(0,0,0,.35)}
.hero-photo{width:500px;height:305px;background:linear-gradient(110deg,#efe4d2 0%,#9a4a2c 32%,#b85a3a 48%,#6f8a3a 62%,#c98b52 85%,#e4b27a 100%)}
.main-nav{position:absolute;left:0;top:385px;width:959px;height:55px;background:var(--nav-band);display:flex;align-items:center;padding-left:21px;gap:29px}
.main-nav a{font-family:"Ubuntu",sans-serif;font-size:19px;color:var(--nav-text);text-decoration:none}
.content-panel{position:absolute;left:20px;top:472px;width:921px;height:607px;background:var(--panel)}
.content-panel::before,.content-panel::after{content:"";position:absolute;left:0;width:921px;height:9px;background-size:14px 9px}
.content-panel::before{top:-9px;background-image:linear-gradient(45deg,var(--panel) 50%,transparent 50%),linear-gradient(-45deg,var(--panel) 50%,transparent 50%)}
.content-panel::after{bottom:-9px;background-image:linear-gradient(135deg,var(--panel) 50%,transparent 50%),linear-gradient(-135deg,var(--panel) 50%,transparent 50%)}
.sidebar{position:absolute;left:12px;top:18px;width:236px}
.side-title{font-family:"Ubuntu",sans-serif;font-size:13.5px;color:#222;margin-bottom:6px}
.class-card{width:236px;height:182px;background:var(--paper);padding:12px 14px 0 15px;font-size:10.6px;line-height:15.6px;text-align:justify;color:#333}
.more{display:block;text-align:right;font-size:10.5px;color:#333}
.cook-card{margin-top:15px;width:233px;height:226px;background:linear-gradient(var(--sun-top),var(--sun-bottom));padding:5px 12px 0 12px}
.cook-card h3{font-family:"Ubuntu",sans-serif;font-weight:400;font-size:14.5px;color:#222;margin-bottom:5px}
.cook-photo{width:209px;height:75px;background:linear-gradient(90deg,#3d63a8,#7fa0d6 55%,#c8a58f)}
.cook-card p{font-size:10.6px;line-height:15.6px;color:#333;text-align:justify;margin-top:7px}
.question-card{margin-top:20px;width:230px;height:108px;background:linear-gradient(var(--leaf-top),var(--leaf-bottom));padding:6px 8px 0 78px;text-align:center;color:#fff}
.question-card .kicker{font-size:10.5px}
.question-card .label{font-family:"Ubuntu",sans-serif;font-size:14px;color:#2f3b1a;letter-spacing:.5px}
.question-card p{font-size:10.6px;line-height:13px;color:#2f3b1a;margin-top:2px}
.posts{position:absolute;left:258px;top:14px;width:642px}
.post h2{font-family:"Ubuntu",sans-serif;font-weight:400;font-size:23px;color:#222;line-height:1.2}
.post-meta{font-size:11.5px;color:#333;padding-bottom:6px;border-bottom:1px dotted var(--rule);margin-top:3px}
.post-body{font-size:11.6px;line-height:17.5px;color:var(--muted);margin-top:12px}
.post + .post{margin-top:20px;position:relative}
.read-more{font-size:11.6px;color:#333;text-align:right}
.post .read-more.top{position:absolute;right:8px;top:25px}
.post-body .gap{height:17.5px}
.site-footer{position:absolute;left:0;top:1110px;width:959px;height:68px;background:var(--footer);color:#fff;font-size:11px}
.social{position:absolute;left:21px;top:27px;display:flex;gap:18px}
.social span{display:flex;align-items:center;gap:4px}
.social i{width:14px;height:14px;background:#5a7fb5;display:inline-block}
.social span + span i{background:#5ab3e0}
.legal{position:absolute;right:21px;top:17px;text-align:right;line-height:16px;font-size:10.5px}
.footer-base{position:absolute;left:0;top:1178px;width:959px;height:22px;background:var(--footer-base)}
</style>
</head>
<body>
<header class="site-header">
  <div class="brand">
    <div class="brand-name">SPRIG UP</div>
    <div class="brand-band">TASTE OF THE MEDITERRANEAN &amp; MIDDLE EAST</div>
  </div>
  <form class="subscribe">
    <div class="subscribe-title">Subscribe to our Mailing List</div>
    <div class="subscribe-field">Enter Email Address</div>
  </form>
  <div class="hero-frame">
    <div class="hero-photo" role="img" aria-label="Plate of falafel on hummus with tabbouleh, tomato salad and flatbread"></div>
  </div>
</header>

<nav class="main-nav">
  <a href="#">Home</a>
  <a href="#">Why Mediterranean &amp; Mid East Cuisine?</a>
  <a href="#">Cooking Class</a>
  <a href="#">Healthy Receipes</a>
  <a href="#">Cooking</a>
  <a href="#">Contact</a>
</nav>

<main class="content-panel">
  <aside class="sidebar">
    <div class="side-title">Register For A Cooking Class</div>
    <div class="class-card">
      Learn to cook the simple, exotic and vibrant cuisine of the Middle East. Class includes the how to’s and techniques of Middle Eastern cooking, the ins and outs on locating and buying ingredients as well as a discussion on the nutritional information. All classes conclude with a three course meal…that you learned to cook of course!
      <span class="more">more...</span>
    </div>
    <div class="cook-card">
      <h3>Meet Leyla The Cook</h3>
      <div class="cook-photo" role="img" aria-label="Portrait of the cook by a seaside village"></div>
      <p>With my Mediterranean roots, I want to bring the authentic, healthy and delicious recipes of the Mediterranean in an easy to do fashion. I am lucky to have garnered an in depth culinary experience from working in my mom’s own catering company and...</p>
      <span class="more">more...</span>
    </div>
    <div class="question-card">
      <div class="kicker">Suggestion and</div>
      <div class="label">QUESTION BOX</div>
      <p>If you have a suggestion for a recipe or any questions, we would be glad to hear it! Just write it in the box and hit submit :)</p>
    </div>
  </aside>

  <section class="posts">
    <article class="post">
      <h2>Spring Dates</h2>
      <div class="post-meta">Posted on January 24, 2012 in: Post, Uncategorized</div>
      <div class="post-body">
        February 19: 6:30pm-9:30pm at Hearth Studio: 72 Harrow Street, Brookvale, NY<br>
        March 17: 10:00am-1:00pm- at Larder Loft: 940 Marlowe Avenue at 18th Street, Brookvale, NY<br>
        March 17: 1:30pm-4:30pm- at Larder Loft: 940 Marlowe Avenue at 18th Street, Brookvale, NY<br>
        March 24: 10:00am-1:00pm- at Larder Loft: 940 Marlowe Avenue at 18th Street, Brookvale, NY<br>
        March 24: 1:30pm-4:30pm- at Larder Loft: 940 Marlowe Avenue at 18th Street, Brookvale, NY- SOLD OUT<br>
        April 14: 10:00am-1:00pm- at Larder Loft: 940 Marlowe Avenue at 18th Street, Brookvale, NY<br>
        April 14: 1:30pm-4:30pm- at Larder Loft: 940 Marlowe Avenue at 18th Street, Brookvale, NY
      </div>
    </article>
    <article class="post">
      <h2>More Cooking Class Dates :)</h2>
      <div class="read-more top">Read More...</div>
      <div class="post-meta">Posted on December 14, 2011 in: Post</div>
      <div class="post-body">
        I always look forward to the classes and have enjoyed meeting so many great people. Look forward to having more and meeting more wonderful people!<br>
        January-<br>
        Jan 28- 12:00pm- 3:00pm- at Hearth Studio: 68 Harrow Street at Linden Avenue, Brookvale, NY SOLD OUT<br>
        <div class="gap"></div>
        February-<br>
        Feb 5- 6:00pm- 9:00pm- at Hearth Studio: 68 Harrow Street at Linden Avenue, Brookvale, NY<br>
        Feb 12- 6:00pm-9:00pm- at Hearth Studio: 68 Harrow Street at Linden Avenue, Brookvale, NY SOLD OUT<br>
        Feb 16- 6:30pm- 9:30pm- at Larder Loft: 940 Marlowe Avenue at 18th Street, Brookvale, NY<br>
        Feb 26- 6:00pm- 9:00pm- at Larder Loft: 940 Marlowe Avenue at 18th Street, Brookvale, NY SOLD OUT<br>
        Feb 29- 6:30pm- 9:30pm- at Larder Loft: 940 Marlowe Avenue at 18th Street, Brookvale, NY<br>
        <div class="gap"></div>
        Just email info@plumhavenkitchen.com with dates selected and you will receive confirmation :0)<br>
        - Leyla
      </div>
      <div class="read-more">Read More...</div>
    </article>
  </section>
</main>

<footer class="site-footer">
  <div class="social">
    <span><i></i>Follow us on Circlewall</span>
    <span><i></i>Follow us on Chirpline</span>
  </div>
  <div class="legal">© 2012 Sprig up. All Rights Reserved.<br>X 30</div>
</footer>
<div class="footer-base"></div>
</body>
</html>
```